make a fireworks website

we are manufacturer of fireworks in Asia.
we need a HD fireworks website for showing product to all world customers.
we also need an register for member system,location, forum,products..etc
I added my Logo for the company.
brightpeonyhall.com.hk

and please message me if you have
any question.
here some example of website:
http://www.lanternmoth.com/
http://www.korvelmist.com/
http://www.tindle-orbwick.co.uk/
http://www.pemberlyspark.co.uk/

```html
<!DOCTYPE html>
<html lang="en">
<head>
<meta charset="utf-8">
<title>Bright Peony Hall — Fireworks</title>
<link href="https://fonts.googleapis.com/css2?family=Open+Sans:ital,wght@0,400;0,600;1,400&family=Open+Sans+Condensed:wght@700&display=swap" rel="stylesheet">
<style>
:root{
  --night:#0b0508;
  --panel:#ffffff;
  --purple:#5a1f9b;
  --red:#c8103b;
  --red-dark:#a30c2f;
  --gold:#f2b84a;
  --cream:#fbe3a3;
  --text:#6b6b6b;
  --ink:#2a2a2a;
  --line:#e2e2e2;
  --grey-btn:#555;
  --foot-text:#9a9a9a;
}
*{margin:0;padding:0;box-sizing:border-box}
html,body{width:807px;height:1200px;overflow:hidden;background:var(--night)}
body{position:relative;font-family:"Open Sans",sans-serif;color:var(--text)}
.abs{position:absolute}
.hero{left:0;top:0;width:807px;height:436px;
  background:radial-gradient(ellipse at 70% 30%,#d64ab0 0%,#7a2a9e 30%,transparent 60%),
  linear-gradient(180deg,#2a1240 0%,#6b2a8a 35%,#c85a9a 60%,#f08a5a 82%,#3a1a10 100%)}
.hero-arrow{width:39px;height:51px;top:211px;background:rgba(0,0,0,.45);display:flex;align-items:center;justify-content:center}
.logo{left:66px;top:0;width:155px;height:85px;background:var(--panel);display:flex;align-items:center;justify-content:center;gap:6px}
.logo span{font-weight:600;font-size:11px;color:var(--purple);white-space:nowrap}
.logo i{width:12px;height:12px;border-radius:50%;background:var(--red);display:block}
.call{left:420px;top:13px;font-size:13px;color:#fff;font-weight:600;white-space:nowrap}
.call b{color:var(--gold);font-weight:600;margin-left:4px}
.search{left:555px;top:10px;width:135px;height:25px;border:1px solid var(--gold);background:rgba(0,0,0,.5);font-size:9px;color:#ccc;padding:6px 9px}
.bag{left:698px;top:10px;width:29px;height:25px;background:#d0208f;display:flex;align-items:center;justify-content:center}
.nav{left:222px;top:46px;width:518px;height:39px;background:rgba(20,10,20,.55);display:flex;justify-content:space-around;align-items:center;padding:0 8px;font-size:11.5px;color:#fff;border-top:1px solid rgba(255,255,255,.15);white-space:nowrap}
.nav .on{color:var(--gold)}
.panel{left:66px;top:436px;width:674px;height:552px;background:var(--panel)}
.band{left:66px;top:436px;width:674px;height:46px;background:var(--cream);display:flex;align-items:center;justify-content:center;gap:12px}
.band h2{font-family:"Open Sans Condensed",sans-serif;font-size:17px;color:var(--red-dark);white-space:nowrap}
.btn{background:var(--red);color:#fff;font-family:"Open Sans Condensed",sans-serif;font-size:13px;display:flex;align-items:center;justify-content:space-between;gap:8px;padding:0 8px 0 10px;border-radius:2px;white-space:nowrap}
.btn:after{content:"";flex:none;width:8px;height:8px;border-radius:50%;border:1px solid rgba(255,255,255,.6);background:rgba(255,255,255,.25)}
.h{font-family:"Open Sans Condensed",sans-serif;font-size:20px;color:var(--purple);line-height:1;white-space:nowrap}
.p{font-size:8.6px;line-height:15.5px}
.photo{border-radius:1px}
.tag{background:var(--grey-btn);color:#eee;font-size:7.6px;height:15px;padding:2px 6px;line-height:11px;white-space:nowrap}
.prod{width:128px;height:79px;border:1px solid var(--line)}
.prod div{position:absolute;left:36px;top:18px;width:56px;height:42px;background:linear-gradient(135deg,#d23a3a,#3a6ac8 60%,#f0c040);border-radius:2px}
.plabel{width:128px;text-align:center;font-size:9.5px;color:var(--red)}
.rule{height:1px;background:var(--line)}
.news{font-size:9px;color:var(--ink);line-height:13px;width:140px}
.date{font-size:8.5px;color:var(--text)}
.testi{left:327px;top:900px;width:403px;height:58px;border:1px solid var(--line);padding:8px 13px}
.testi q{font-style:italic;font-size:8.4px;color:var(--ink);line-height:13px;display:block}
.testi p{font-size:8.5px;margin-top:7px}
.footer{left:0;top:988px;width:807px;height:212px;background:linear-gradient(180deg,#0e0c10 0%,#15141a 55%,#2a1e16 78%,#0b0908 100%)}
.fh{font-size:10px;color:#e8e8e8;white-space:nowrap}
.fl{font-size:8.2px;color:var(--foot-text);line-height:16.8px;white-space:nowrap}
.field{left:522px;width:156px;background:#2b2b2b;border:1px solid #444;font-size:8.2px;color:#aaa;padding:6px 8px;border-radius:2px}
.submit{left:684px;top:1112px;width:42px;height:20px;background:#6a6a6a;color:#eee;font-size:8px;display:flex;align-items:center;justify-content:center;border-radius:2px}
.soc{top:1112px;width:19px;height:19px;background:#8a8a8a;border-radius:2px}
.copy{left:0;top:1174px;width:807px;text-align:center;font-size:8.2px;color:var(--foot-text)}
</style>
</head>
<body>
<div class="abs hero" role="img" aria-label="Family silhouette watching pink and purple fireworks over a sunset field"></div>
<div class="abs hero-arrow" style="left:0"><svg width="14" height="26"><path d="M12 2 2 13l10 11" stroke="#fff" stroke-width="1.5" fill="none"/></svg></div>
<div class="abs hero-arrow" style="left:768px"><svg width="14" height="26"><path d="M2 2l10 11L2 24" stroke="#fff" stroke-width="1.5" fill="none"/></svg></div>

<header>
  <div class="abs logo"><i></i><span>brightpeonyhall.com.hk</span></div>
  <div class="abs call">Call us<b>555 014 2736</b></div>
  <div class="abs search">Search
    <svg class="abs" style="right:6px;top:4px" width="16" height="16"><circle cx="7" cy="7" r="5" stroke="#f2b84a" stroke-width="2" fill="none"/><path d="M11 11l4 4" stroke="#f2b84a" stroke-width="2.5"/></svg>
  </div>
  <div class="abs bag"><svg width="14" height="14"><rect x="1" y="5" width="12" height="9" fill="#fff"/><path d="M4 6V3a3 3 0 0 1 6 0v3" stroke="#fff" stroke-width="1.5" fill="none"/></svg></div>
  <nav class="abs nav"><span class="on">HOME</span><span>ABOUT US</span><span>SERVICES</span><span>PRODUCTS</span><span>OFFERS</span><span>CONTACT US</span></nav>
</header>

<main>
  <div class="abs panel"></div>
  <div class="abs band"><h2>Morbi et mi sit amet nulla semper faucibus pharetra nec ante.</h2><div class="btn" style="height:25px">Start Shopping</div></div>

  <h2 class="abs h" style="left:78px;top:508px;font-size:19px">Welcome to Bright Peony Hall</h2>
  <p class="abs p" style="left:78px;top:534px;width:236px">Sed tristique magna vel diam feugiat rutrum. Praesent commodo faucibus porta. Donec velit nibh, congue eu facilisis id, adipiscing id mi. Vestibulum sagittis tempor nibh, vel elementum enim luctus sit amet. Aliquam pretium velit dolor, sed ultrices tortor dapibus vitae.</p>
  <div class="abs photo" style="left:78px;top:622px;width:233px;height:132px;background:radial-gradient(circle at 50% 45%,#7a2030,#1a0a14 70%)" role="img" aria-label="Father holding daughter on his shoulders under fireworks"></div>

  <h2 class="abs h" style="left:328px;top:508px">Our Products</h2>
  <div class="abs tag" style="left:652px;top:510px">View all products</div>
  <div class="abs prod" style="left:328px;top:539px" role="img" aria-label="Cake firework box"><div></div></div>
  <div class="abs prod" style="left:465px;top:539px" role="img" aria-label="Mortar tube firework"><div></div></div>
  <div class="abs prod" style="left:602px;top:539px" role="img" aria-label="Rocket assortment"><div></div></div>
  <div class="abs prod" style="left:328px;top:652px" role="img" aria-label="Firecracker bundle"><div></div></div>
  <div class="abs prod" style="left:465px;top:652px" role="img" aria-label="Fountain firework pack"><div></div></div>
  <div class="abs prod" style="left:602px;top:652px" role="img" aria-label="Boxed shell set"><div></div></div>
  <div class="abs plabel" style="left:328px;top:622px">Mauris iaculis</div>
  <div class="abs plabel" style="left:465px;top:622px">Mauris iaculis</div>
  <div class="abs plabel" style="left:602px;top:622px">Mauris iaculis</div>
  <div class="abs plabel" style="left:328px;top:735px">Mauris iaculis</div>
  <div class="abs plabel" style="left:465px;top:735px">Mauris iaculis</div>
  <div class="abs plabel" style="left:602px;top:735px">Mauris iaculis</div>

  <div class="abs rule" style="left:78px;top:778px;width:234px"></div>
  <div class="abs rule" style="left:327px;top:778px;width:403px"></div>

  <h2 class="abs h" style="left:78px;top:796px">Latest News &amp; Events</h2>
  <div class="abs photo" style="left:78px;top:828px;width:86px;height:56px;background:radial-gradient(circle at 50% 40%,#5a3aa0,#0a0a1a 70%)" role="img" aria-label="Fireworks burst at night"></div>
  <p class="abs news" style="left:174px;top:826px">Curabitur non ante viverra, lacinia massa ac, pulvinar nibh et quam sollicitudin.</p>
  <p class="abs date" style="left:174px;top:870px">June 1, 2014</p>
  <div class="abs photo" style="left:78px;top:902px;width:86px;height:56px;background:linear-gradient(180deg,#2a3040,#5a5a3a 55%,#101418)" role="img" aria-label="Fireworks over a harbour at night"></div>
  <p class="abs news" style="left:174px;top:900px">Curabitur non ante viverra, lacinia massa ac, pulvinar nibh et quam sollicitudin.</p>
  <p class="abs date" style="left:174px;top:944px">June 1, 2014</p>

  <h2 class="abs h" style="left:328px;top:796px">Fireworks Service for...</h2>
  <div class="abs btn" style="left:327px;top:828px;width:88px;height:26px">Wedding</div>
  <div class="abs btn" style="left:423px;top:828px;width:88px;height:26px">Corporate</div>
  <div class="abs btn" style="left:519px;top:828px;width:88px;height:26px">Public</div>
  <div class="abs btn" style="left:615px;top:828px;width:88px;height:26px">Parties</div>

  <h2 class="abs h" style="left:328px;top:873px">Client’s Testimonials</h2>
  <div class="abs tag" style="left:639px;top:876px">View all testimonials</div>
  <div class="abs testi"><q>Praesent rutrum elementum elit, eget tincidunt massa interdum sit amet. Integer pel lentesque lacus magna, et pretium leo vestibulum eu.</q><p>John Doe, NY</p></div>
</main>

<footer>
  <div class="abs footer"></div>
  <h3 class="abs fh" style="left:82px;top:1004px;font-weight:400">Navigation Menu</h3>
  <div class="abs fl" style="left:82px;top:1026px">Home<br>About us<br>Services<br>Our Products</div>
  <div class="abs fl" style="left:159px;top:1026px">Offers<br>Contact us<br>Register<br>Login</div>
  <h3 class="abs fh" style="left:257px;top:1004px;font-weight:400">Support Links</h3>
  <div class="abs fl" style="left:257px;top:1026px">Privacy Policy<br>Terms and Conditions<br>Customer Support<br>FAQ</div>
  <h3 class="abs fh" style="left:412px;top:1004px;font-weight:400">Fireworks for</h3>
  <div class="abs fl" style="left:412px;top:1026px">Wedding<br>Corporate<br>Public<br>Parties</div>
  <h3 class="abs fh" style="left:524px;top:1004px;font-weight:400">Contact us</h3>
  <div class="abs field" style="top:1032px;height:24px">Name</div>
  <div class="abs field" style="top:1060px;height:24px">E-mail</div>
  <div class="abs field" style="top:1088px;height:45px">Comment</div>
  <div class="abs submit">SUBMIT</div>
  <div class="abs soc" style="left:82px"></div>
  <div class="abs soc" style="left:105px"></div>
  <div class="abs soc" style="left:128px"></div>
  <div class="abs soc" style="left:151px"></div>
  <div class="abs soc" style="left:174px"></div>
  <p class="abs copy">Copyright © 2014 Bright Peony Hall. All rights reserved.</p>
</footer>
</body>
</html>
```